Looking for a label design for a product call KAVA. My business is to sell prepack kava to stores and online.
I need Hawaiian Polynesian theme around tradition.

The label need to have "Nalu Kava" that's the name of the product. Can add "traditional herbal drink"

Can be colorful, the label will be print in a oval shape clear label size 4.25"x3.25" and will be put on a black back ground.

I don't want any white.

Target Market(s)

Polynesian population and tourist

Industry/Entity Type

Business

Requirements
Must have
• Name: Nalu Kava
inscription: Traditional Herbal drink
inscription: 100% Dried Powder Kava Roots
Net Wt: 8oz
Nice to have
• Traditional art design.

```html
<!DOCTYPE html>
<html lang="en">
<head>
<meta charset="utf-8">
<title>Nalu Kava – Label</title>
<link rel="stylesheet" href="https://fonts.googleapis.com/css2?family=Fredoka:wght@600;700&family=Baloo+2:wght@500;600&display=swap">
<style>
  :root {
    --bg-edge: #2a2a2a;
    --bg-center: #464646;
    --label-black: #2b2b2b;
    --panel-black: #1f1f1f;
    --gold-light: #fcd14a;
    --gold: #f2b01c;
    --gold-deep: #d8860e;
    --ink: #2a2622;
    --text-gold: #f5bd22;
  }
  html, body {
    margin: 0;
    padding: 0;
    width: 1200px;
    height: 1000px;
    overflow: hidden;
    background: var(--bg-edge);
  }
  .canvas {
    display: block;
    width: 1200px;
    height: 1000px;
  }
  .brand-name {
    font-family: "Fredoka", "Baloo 2", sans-serif;
    font-weight: 700;
    fill: var(--ink);
  }
  .tagline, .ingredients, .net-label, .net-value {
    font-family: "Baloo 2", "Fredoka", sans-serif;
    fill: var(--text-gold);
  }
  .tagline { font-weight: 500; font-size: 37px; }
  .ingredients { font-weight: 500; font-size: 24px; }
  .net-label { font-weight: 500; font-size: 26px; }
  .net-value { font-family: "Fredoka", sans-serif; font-weight: 600; font-size: 68px; }
</style>
</head>
<body>
<svg class="canvas" viewBox="0 0 1200 1000" xmlns="http://www.w3.org/2000/svg">
  <defs>
    <linearGradient id="backdrop" x1="0" x2="1" y1="0" y2="0">
      <stop offset="0" stop-color="var(--bg-edge)"/>
      <stop offset="0.5" stop-color="var(--bg-center)"/>
      <stop offset="1" stop-color="var(--bg-edge)"/>
    </linearGradient>
    <linearGradient id="gold-ring" x1="0" x2="1" y1="0" y2="1">
      <stop offset="0" stop-color="var(--gold-light)"/>
      <stop offset="0.5" stop-color="var(--gold)"/>
      <stop offset="1" stop-color="var(--gold-deep)"/>
    </linearGradient>
    <radialGradient id="gold-panel" cx="0.5" cy="0.45" r="0.6">
      <stop offset="0" stop-color="var(--gold-light)"/>
      <stop offset="0.6" stop-color="var(--gold)"/>
      <stop offset="1" stop-color="var(--gold-deep)"/>
    </radialGradient>
    <linearGradient id="crest-tone" x1="0" x2="0" y1="0" y2="1">
      <stop offset="0" stop-color="var(--gold-deep)"/>
      <stop offset="1" stop-color="#8a5a12"/>
    </linearGradient>
    <clipPath id="inner-oval">
      <ellipse cx="600" cy="500" rx="238" ry="323"/>
    </clipPath>
  </defs>

  <rect class="backdrop" width="1200" height="1000" fill="url(#backdrop)"/>

  <g class="label">
    <ellipse class="label-outline" cx="600" cy="500" rx="277" ry="362" fill="var(--label-black)"/>
    <ellipse class="label-ring" cx="600" cy="500" rx="257" ry="342" fill="url(#gold-ring)"/>
    <ellipse class="label-inner-edge" cx="600" cy="500" rx="243" ry="328" fill="var(--panel-black)"/>

    <g clip-path="url(#inner-oval)">
      <rect class="upper-panel" x="360" y="170" width="480" height="410" fill="url(#gold-panel)"
            role="img" aria-label="Gold damask floral pattern background"/>
      <path class="lower-panel" d="M340 576 Q600 584 860 576 L860 840 L340 840 Z" fill="var(--panel-black)"/>
      <path class="panel-divider" d="M340 576 Q600 584 860 576" fill="none" stroke="var(--gold-light)" stroke-width="3"/>
    </g>

    <rect class="crest-placeholder" x="455" y="145" width="290" height="185" rx="14"
          fill="url(#crest-tone)" opacity="0.85"
          role="img" aria-label="Carved Polynesian tiki crest with scrolling ornaments in black and gold"/>

    <text class="brand-name" x="605" y="420" font-size="94" text-anchor="middle" letter-spacing="3">NALU</text>
    <text class="brand-name" x="621" y="548" font-size="156" text-anchor="middle" letter-spacing="4">KAVA</text>

    <text class="tagline" x="601" y="641" text-anchor="middle">Traditional Herbal Drink</text>
    <text class="ingredients" x="601" y="670" text-anchor="middle">100% Dried Powder Kava Roots</text>
    <text class="net-label" x="600" y="714" text-anchor="middle">Net Wt:</text>
    <text class="net-value" x="601" y="773" text-anchor="middle">8oz</text>
  </g>
</svg>
</body>
</html>
```